Financial PR company Homepage and Inner Page design

Please design a web homepage and innerpage for OVIN Public Relations.
OVIN Public Relations is a Financial PR company targeting Shenzhen Qian Special Economical Zone.
Note:
1. Menu includes ( Please specialize in Chinese and we want to see the Chinese fonts)
关于我们/服务板块/专业优势/合作伙伴/前海商圈/公司新闻/加盟我们/联系我们

2. Please refer to world class PR Business company and contribute your idea on website design and color themes.

3. We have attached the Logo for reference.

4. Anytime use picture for reference, please select asian business people pictures.

Cheers,

HI Designers, Thanks for the design submission. Here is our client feedback: 1. Adopt one screen design. 2. Use amiable Asia Business woman pictures. 3. Use contrastive color theme for the design. Cheers, Kip From TW

```html
<!DOCTYPE html>
<html lang="en">
<head>
<meta charset="utf-8">
<title>OVIN Public Relations</title>
<link href="https://fonts.googleapis.com/css2?family=Ubuntu:wght@400;500;700&family=Arimo:wght@400;700&family=Noto+Sans+SC:wght@400;700&display=swap" rel="stylesheet">
<style>
:root{
  --navy:#10213a;
  --navy-deep:#0b1829;
  --blue:#0a9be0;
  --blue-light:#36b8f2;
  --white:#ffffff;
  --page:#e2e2e2;
  --card:#f2f2f2;
  --ink:#222;
  --heading:#333;
  --foot-top:#8e8e8e;
  --foot-bot:#6a6a6a;
}
*{margin:0;padding:0;box-sizing:border-box}
html,body{width:1200px;height:1003px;overflow:hidden}
body{background:var(--page);font-family:"Arimo",Arial,sans-serif;position:relative}

.site-header{position:absolute;left:0;top:0;width:1200px;height:91px;background:var(--navy)}
.brand{position:absolute;left:135px;top:18px;display:flex;align-items:center;gap:12px}
.brand-mark{width:40px;height:40px;border-radius:50%;background:var(--blue-light)}
.brand-name{font-family:"Ubuntu",sans-serif;font-size:34px;font-weight:400;color:var(--white);letter-spacing:.5px}
.client-area{position:absolute;left:970px;top:0;width:111px;height:21px;background:#f4f4f4;border-radius:0 0 4px 4px;
  font-family:"Ubuntu",sans-serif;font-size:13px;color:#333;text-align:center;line-height:20px}
.main-nav{position:absolute;left:397px;top:0;height:91px;display:flex;align-items:center;
  font-family:"Ubuntu",sans-serif;font-size:12px;color:var(--white);text-transform:uppercase}
.main-nav a{color:var(--white);text-decoration:none}
.main-nav .sep{margin:0 6px}
.main-nav .current{display:block;width:52px;height:91px;line-height:100px;text-align:center;margin-right:8px;
  background:linear-gradient(#38bdf5,#0b8fd6)}

.hero{position:absolute;left:0;top:91px;width:1200px;height:397px;
  background:linear-gradient(180deg,#7fb0d6 0%,#b7d3e8 35%,#8a7d6c 55%,#6e5a48 72%,#5d7a8e 82%,#8fb0c6 100%)}
.hero-arrow{position:absolute;top:170px;width:36px;height:36px}
.hero-arrow.prev{left:151px}
.hero-arrow.next{left:1013px}
.hero-caption{position:absolute;left:554px;top:300px;width:280px;height:67px;background:rgba(40,40,40,.55);
  font-family:"Noto Sans SC",sans-serif;font-size:30px;color:var(--white);line-height:67px;text-align:center;
  text-shadow:1px 1px 3px rgba(0,0,0,.7)}

.features{position:absolute;left:0;top:488px;width:1200px;height:109px;display:flex}
.feature{position:relative;height:109px;background:linear-gradient(135deg,#1b2a3c,#0c1622 60%,#243241)}
.feature.highlight{background:var(--blue)}
.feature svg{position:absolute}
.feature h2{position:absolute;font-family:"Ubuntu",sans-serif;font-weight:700;font-size:15px;color:var(--white);top:18px}
.feature p{position:absolute;font-size:11.5px;line-height:15.5px;color:var(--white);top:42px;width:200px}
.feature.highlight p{color:#e4f4ff}

.welcome{position:absolute;left:131px;top:636px;width:938px;height:251px;background:var(--white);border-radius:8px;
  box-shadow:0 18px 14px -14px rgba(0,0,0,.35)}
.welcome-inner{position:absolute;left:10px;top:9px;width:918px;height:232px;background:var(--card);border-radius:8px}
.welcome h1{position:absolute;left:9px;top:20px;font-size:19px;font-weight:400;color:var(--heading)}
.welcome-text{position:absolute;left:9px;top:52px;width:606px;font-size:11.5px;line-height:20.6px;color:var(--ink);letter-spacing:.5px}
.welcome-text p+p{margin-top:20.6px}
.welcome-photo{position:absolute;left:630px;top:62px;width:278px;height:130px;
  background:linear-gradient(90deg,#5a2a3c,#3c4a46 40%,#6c5a4a 70%,#2a2f4a)}

.site-footer{position:absolute;left:0;top:931px;width:1200px;height:72px;background:linear-gradient(var(--foot-top),var(--foot-bot))}
.footer-nav{position:absolute;left:145px;top:14px;font-family:"Noto Sans SC",sans-serif;font-size:11px;font-weight:700;color:var(--white)}
.footer-nav .sep{margin:0 6px}
.copyright{position:absolute;left:145px;top:41px;font-size:11.5px;color:var(--white)}
</style>
</head>
<body>
<header class="site-header">
  <div class="brand"><span class="brand-mark"></span><span class="brand-name">OVIN PR</span></div>
  <div class="client-area">Client Area</div>
  <nav class="main-nav">
    <a class="current" href="#">Home</a>
    <a href="#">About us</a><span class="sep">/</span>
    <a href="#">Service</a><span class="sep">/</span>
    <a href="#">Our advantage</a><span class="sep">/</span>
    <a href="#">Parters</a><span class="sep">/</span>
    <a href="#">Qianhai</a><span class="sep">/</span>
    <a href="#">Company news</a><span class="sep">/</span>
    <a href="#">Join us</a><span class="sep">/</span>
    <a href="#">Contact us</a>
  </nav>
</header>

<section class="hero" role="img" aria-label="City skyline of high-rise towers rising above water under a blue sky">
  <svg class="hero-arrow prev" viewBox="0 0 36 36"><circle cx="18" cy="18" r="18" fill="rgba(255,255,255,.15)"/><path d="M21 10 L13 18 L21 26" stroke="#fff" stroke-width="4" fill="none"/></svg>
  <svg class="hero-arrow next" viewBox="0 0 36 36"><circle cx="18" cy="18" r="18" fill="rgba(255,255,255,.15)"/><path d="M15 10 L23 18 L15 26" stroke="#fff" stroke-width="4" fill="none"/></svg>
  <div class="hero-caption">简单是终极的复杂</div>
</section>

<section class="features">
  <div class="feature" style="width:452px">
    <svg style="left:151px;top:38px" width="68" height="48" viewBox="0 0 68 48" fill="none" stroke="#fff" stroke-width="3">
      <path d="M2 46 V28 H10"/><path d="M14 46 V4 H34 V46"/><path d="M34 16 H44 V46"/><path d="M50 30 H56 V46"/>
      <rect x="20" y="10" width="3" height="3" fill="#fff"/><rect x="27" y="18" width="3" height="3" fill="#fff"/>
    </svg>
    <h2 style="left:231px">ABOUT US</h2>
    <p style="left:231px">Lorem Ipsum is simply dummy text of printing and typesetting indus Lorem Ipsum has been the standa</p>
  </div>
  <div class="feature highlight" style="width:304px">
    <svg style="left:30px;top:36px" width="40" height="54" viewBox="0 0 40 54" fill="#fff">
      <path d="M6 2 H12 V6 H16 V2 H24 V6 H28 V2 H34 V14 H6 Z"/><path d="M9 18 H31 L34 44 H6 Z" fill="none" stroke="#fff" stroke-width="3"/><rect x="2" y="46" width="36" height="7"/>
    </svg>
    <h2 style="left:93px">OUR STRATEGY</h2>
    <p style="left:93px">Lorem Ipsum is simply dummy text of printing and typesetting indus Lorem Ipsum has been the standa</p>
  </div>
  <div class="feature" style="width:444px">
    <svg style="left:20px;top:42px" width="66" height="44" viewBox="0 0 66 44" fill="#fff">
      <circle cx="14" cy="10" r="7"/><path d="M2 44 V28 Q2 20 14 20 Q26 20 26 28 V44 Z"/>
      <circle cx="52" cy="10" r="7"/><path d="M40 44 V28 Q40 20 52 20 Q64 20 64 28 V44 Z"/>
      <circle cx="33" cy="8" r="8"/><path d="M19 44 V26 Q19 18 33 18 Q47 18 47 26 V44 Z"/>
    </svg>
    <h2 style="left:95px">MEET THE TEAM</h2>
    <p style="left:95px">Lorem Ipsum is simply dummy text of printing and typesetting indus Lorem Ipsum has been the standa</p>
  </div>
</section>

<section class="welcome">
  <div class="welcome-inner">
    <h1>Welcome to OVIN Public Relations</h1>
    <div class="welcome-text">
      <p>Lorem ipsum dolor sit amet, consectetur adipiscing elit. Proin pulvinar eros in imperdiet porttitor. Praesent velit justo, placerat ut ornare aliquet, venenatis vel justo. Nulla porttitor enim vitae nibh scelerisque, nec laoreet libero posuere. Integer ut neque ut purus dictum auctor. Cras tincidunt odio a pharetra iaculis. Nam in arcu eu tortor consequat tempor. Vivamus eu convallis risus.</p>
      <p>Mauris pulvinar, eros ac elementum tempus, enim metus vehicula ante, ut scelerisque ipsum libero non sem. Integer a commodo augue. Ut accumsan efficitur mattis. Donec ut mollis nisl. Suspendisse tincidunt</p>
    </div>
    <div class="welcome-photo" role="img" aria-label="Row of classical stone columns on a lit building facade at night"></div>
  </div>
</section>

<footer class="site-footer">
  <div class="footer-nav">关于我们<span class="sep"></span> 服务板块<span class="sep">/</span>专业优势<span class="sep">/</span>合作伙伴<span class="sep">/</span>前海商圈<span class="sep">/</span>公司新闻<span class="sep">/</span>加盟我们<span class="sep">/</span>联系我们</div>
  <div class="copyright">Copyright © 2014 -&nbsp; OVIN Public Relations - All rights reserved.</div>
</footer>
</body>
</html>
```